French Puns

Creation of a cover for a book on French plays on words.
The public is lovers of the French language
TITLE: The gentle phrases of Honoré Vasseline
SUB-TITLE: Witty words, wit of words
PUBLISHER (at the bottom of the page): Editions Plumeau
(See joined examples, previous books of the same author)
Size: 14 x 20.5 cm
Please note that the text on the cover is in French, not in English:
Fine phrases from Honoré Vasseline
Witty words, witty words (subtitle, smaller)
Plumeau Editions

```html
<!DOCTYPE html>
<html lang="en">
<head>
<meta charset="utf-8">
<title>The gentle phrases of Honoré Vasseline — Editions Plumeau</title>
<link rel="stylesheet" href="https://fonts.googleapis.com/css2?family=Montserrat:wght@700;800&family=Patrick+Hand&display=swap">
<style>
  :root {
    --backdrop: #e6e6e6;
    --paper: #f3f3f3;
    --lavender: #8f86c0;
    --lavender-pale: #b9b3d9;
    --lemon: #e3cc2f;
    --ink: #2b2b2b;
    --rose: #cc5f8f;
    --figure-tone: #e9d9a8;
    --pencil-tone: #ddd6ea;
  }
  * { margin: 0; padding: 0; box-sizing: border-box; }
  html, body {
    width: 1200px; height: 801px; overflow: hidden;
    background: var(--backdrop);
  }
  .cover {
    position: absolute; left: 354px; top: 40px;
    width: 492px; height: 720px;
    background: var(--paper);
    overflow: hidden;
    font-family: "Montserrat", sans-serif;
  }
  .cover__shapes { position: absolute; inset: 0; width: 100%; height: 100%; }
  .title {
    position: absolute; right: 34px; top: 170px;
    text-align: right; font-weight: 800; line-height: 1.08;
  }
  .title__lead { display: block; color: var(--lavender); font-size: 29px; }
  .title__author { display: block; color: var(--lemon); font-size: 33px; }
  .subtitle {
    position: absolute; right: 40px; top: 262px;
    background: var(--lemon); color: #5a4f8c;
    font-family: "Patrick Hand", cursive;
    font-size: 23px; padding: 2px 16px; border-radius: 10px;
  }
  .art { position: absolute; }
  .art--flying-figure {
    left: 70px; top: 320px; width: 210px; height: 120px;
    background: linear-gradient(135deg, var(--figure-tone), #e7c8da);
    border-radius: 60px 50px 70px 40px;
  }
  .art--pencil-character {
    left: 250px; top: 400px; width: 200px; height: 170px;
    background: linear-gradient(135deg, var(--pencil-tone), #f0e4a6);
    border-radius: 40px 90px 70px 60px;
  }
  .publisher {
    position: absolute; left: 96px; bottom: 60px;
    font-weight: 700; font-size: 15px; color: var(--ink);
  }
</style>
</head>
<body>
  <main class="cover">
    <svg class="cover__shapes" viewBox="0 0 492 720" aria-hidden="true">
      <path d="M300 0 H492 V150 C470 120 440 110 420 100 C390 85 330 80 300 45 Z" fill="var(--lemon)"/>
      <path d="M340 40 C380 20 440 30 492 20 V230 C470 210 450 190 440 170 C420 140 350 120 340 90 Z" fill="var(--lavender-pale)"/>
      <path d="M380 90 C420 70 470 80 492 90 V250 C460 240 430 200 410 170 C390 140 370 120 380 90 Z" fill="var(--lavender)"/>
      <circle cx="470" cy="160" r="18" fill="var(--paper)" opacity="0.8"/>
      <path d="M0 110 C60 50 160 20 260 55" fill="none" stroke="var(--ink)" stroke-width="1.5"/>
      <path d="M0 560 C40 545 70 560 80 585 C95 620 70 650 40 660 L0 665 Z" fill="var(--lemon)"/>
      <path d="M0 620 C40 610 90 640 110 670 C125 695 120 710 110 720 H0 Z" fill="var(--lavender)"/>
      <path d="M20 480 C70 500 80 560 60 610 C40 660 120 690 180 650 C230 620 260 660 270 720" fill="none" stroke="var(--ink)" stroke-width="1.3"/>
      <circle cx="52" cy="455" r="14" fill="var(--rose)"/>
      <circle cx="62" cy="555" r="13" fill="var(--rose)"/>
      <path d="M262 632 L272 638 L262 644 Z" fill="var(--ink)"/>
      <circle cx="340" cy="655" r="12" fill="none" stroke="var(--lemon)" stroke-width="4"/>
      <circle cx="344" cy="658" r="9" fill="none" stroke="var(--lavender)" stroke-width="2"/>
      <circle cx="432" cy="565" r="11" fill="none" stroke="var(--lemon)" stroke-width="4"/>
      <circle cx="429" cy="568" r="8" fill="none" stroke="#e08a3a" stroke-width="2"/>
    </svg>

    <h1 class="title">
      <span class="title__lead">The gentle phrases of</span>
      <span class="title__author">Honoré Vasseline</span>
    </h1>
    <p class="subtitle">Witty words, wit of words</p>

    <div class="art art--flying-figure" role="img" aria-label="Illustration of a person leaping beside a speech bubble with a lightbulb"></div>
    <div class="art art--pencil-character" role="img" aria-label="Illustration of a cheerful pencil character with a speech bubble saying witty words, wit of words"></div>

    <p class="publisher">Editions Plumeau</p>
  </main>
</body>
</html>
```